" A clínica já existe há 15 anos, atendendo a classe "C". Já possui uma logo há 8 anos. Este serviço solicitado será para uma nova sede que atenderá o público "A". O produto principal desta nova clínica é o aparelho estético (invisível). "

```html
<!DOCTYPE html>
<html lang="pt-BR">
<head>
<meta charset="utf-8">
<title>Adesivos — Lucas de Vargas Ortodontia Invisível</title>
<link rel="stylesheet" href="https://fonts.googleapis.com/css2?family=Questrial&family=Josefin+Sans:wght@300;400&display=swap">
<style>
  :root {
    --board-light: #d4d4d6;
    --board-dark: #b9b9bc;
    --label: #1a1a1a;
    --paper: #ffffff;
    --paper-shade: #e6e6e8;
    --ink: #111111;
    --ink-soft: #4a4a4a;
    --band-grey: #9c9c9f;
    --on-dark: #e9e9e9;
    --on-dark-soft: #a8a8a8;
    --rule-dark: #4d4d4d;
  }
  html, body {
    margin: 0;
    padding: 0;
    width: 1200px;
    height: 1200px;
    overflow: hidden;
  }
  .board {
    position: relative;
    width: 1200px;
    height: 1200px;
    background: radial-gradient(ellipse at 50% 45%, var(--board-light) 0%, var(--board-dark) 100%);
    font-family: "Questrial", sans-serif;
  }
  .board-label {
    position: absolute;
    left: 31px;
    top: 92px;
    margin: 0;
    font-size: 24px;
    font-weight: 400;
    letter-spacing: 0.5px;
    color: var(--label);
  }
  .stickers {
    position: absolute;
    inset: 0;
  }
  .brand-name { font-family: "Josefin Sans", sans-serif; font-weight: 300; fill: var(--ink); }
  .brand-tag { font-family: "Questrial", sans-serif; fill: var(--ink-soft); }
  .contact { font-family: "Questrial", sans-serif; fill: var(--on-dark); }
  .contact-soft { font-family: "Questrial", sans-serif; fill: var(--on-dark-soft); }
</style>
</head>
<body>
<main class="board">
  <h1 class="board-label">ADESIVOS</h1>

  <svg class="stickers" width="1200" height="1200" viewBox="0 0 1200 1200" xmlns="http://www.w3.org/2000/svg">
    <defs>
      <linearGradient id="paper-fade" x1="0" y1="0" x2="1" y2="1">
        <stop offset="0" stop-color="var(--paper)"/>
        <stop offset="0.5" stop-color="var(--paper-shade)"/>
        <stop offset="1" stop-color="var(--paper)"/>
      </linearGradient>
      <linearGradient id="dark-fade" x1="0" y1="0" x2="0" y2="1">
        <stop offset="0" stop-color="#2a2a2a"/>
        <stop offset="0.4" stop-color="var(--ink)"/>
        <stop offset="1" stop-color="#050505"/>
      </linearGradient>
      <clipPath id="rect-clip">
        <rect x="0" y="0" width="439" height="286" rx="22"/>
      </clipPath>
      <clipPath id="round-clip">
        <circle cx="0" cy="0" r="142"/>
      </clipPath>
    </defs>

    <!-- Rectangular sticker -->
    <g class="sticker sticker-rect" transform="translate(199 446)">
      <rect x="2" y="5" width="439" height="286" rx="22" fill="#000" opacity="0.18"/>
      <g clip-path="url(#rect-clip)">
        <rect class="sticker-face" width="439" height="286" fill="url(#paper-fade)" role="img" aria-label="Fundo claro com ondas suaves em cinza"/>
        <path class="band-grey" d="M0 176 C130 164 300 160 439 156 L439 168 C300 172 140 178 0 190 Z" fill="var(--band-grey)"/>
        <path class="band-dark" d="M0 186 C140 174 300 168 439 165 L439 286 L0 286 Z" fill="url(#dark-fade)"/>
      </g>
      <rect width="439" height="286" rx="22" fill="none" stroke="#cfcfcf" stroke-width="1"/>

      <circle class="brand-mark" cx="219.5" cy="64" r="29" fill="var(--ink)"/>
      <text class="brand-name" x="219.5" y="131" font-size="31" text-anchor="middle" letter-spacing="0.5">LUCAS DE VARGAS</text>
      <line x1="82" y1="149" x2="112" y2="149" stroke="var(--ink-soft)" stroke-width="1"/>
      <text class="brand-tag" x="219.5" y="153" font-size="10.5" text-anchor="middle" textLength="200" lengthAdjust="spacing">ORTODONTIA INVISÍVEL</text>
      <line x1="327" y1="149" x2="357" y2="149" stroke="var(--ink-soft)" stroke-width="1"/>

      <text class="contact" x="219.5" y="216" font-size="12.5" text-anchor="middle">(51) 3456.7020  |  (51) 0000.0000 / 0000.0000</text>
      <line x1="70" y1="228" x2="369" y2="228" stroke="var(--rule-dark)" stroke-width="0.8"/>
      <text class="contact" x="219.5" y="245" font-size="11.5" text-anchor="middle">Rua Dom Vital, 48-302 - Bela Vista - Porto Alegre-RS</text>
      <line x1="70" y1="255" x2="369" y2="255" stroke="var(--rule-dark)" stroke-width="0.8"/>
      <text class="contact-soft" x="219.5" y="272" font-size="11" text-anchor="middle" letter-spacing="3">www.lucasdevargas.com.br</text>
    </g>

    <!-- Round sticker -->
    <g class="sticker sticker-round" transform="translate(835 590)">
      <circle cx="2" cy="5" r="142" fill="#000" opacity="0.18"/>
      <g clip-path="url(#round-clip)">
        <rect x="-142" y="-142" width="284" height="284" fill="url(#paper-fade)" role="img" aria-label="Fundo claro com ondas suaves em cinza"/>
        <path d="M-142 32 C-60 24 60 18 142 14 L142 24 C60 28 -60 34 -142 44 Z" fill="var(--band-grey)"/>
        <path d="M-142 41 C-60 32 60 26 142 22 L142 142 L-142 142 Z" fill="url(#dark-fade)"/>
      </g>
      <circle r="142" fill="none" stroke="#cfcfcf" stroke-width="1"/>

      <circle class="brand-mark" cx="0" cy="-78" r="26" fill="var(--ink)"/>
      <text class="brand-name" x="0" y="-14" font-size="21" text-anchor="middle" letter-spacing="0.4">LUCAS DE VARGAS</text>
      <line x1="-100" y1="1" x2="-76" y2="1" stroke="var(--ink-soft)" stroke-width="0.8"/>
      <text class="brand-tag" x="0" y="4" font-size="7.5" text-anchor="middle" textLength="140" lengthAdjust="spacing">ORTODONTIA INVISÍVEL</text>
      <line x1="76" y1="1" x2="100" y2="1" stroke="var(--ink-soft)" stroke-width="0.8"/>

      <text class="contact" x="0" y="64" font-size="8" text-anchor="middle">(51) 3456.7020  |  (51) 0000.0000 / 0000.0000</text>
      <line x1="-95" y1="73" x2="95" y2="73" stroke="var(--rule-dark)" stroke-width="0.6"/>
      <text class="contact" x="0" y="86" font-size="7" text-anchor="middle">Rua Dom Vital, 48-302 - Bela Vista - Porto Alegre-RS</text>
      <line x1="-90" y1="95" x2="90" y2="95" stroke="var(--rule-dark)" stroke-width="0.6"/>
      <text class="contact-soft" x="0" y="116" font-size="7.5" text-anchor="middle" letter-spacing="2">www.lucasdevargas.com.br</text>
    </g>
  </svg>
</main>
</body>
</html>
```